Tarnby Group letterhead

Hi,

I need a letterhead template created for our business. This should be done in word format and A4 size. The images need to not move in the template ie when I am adding writing in etc. and should flow on when I get to a second page.

I have attached our logo templates below.

Other details to include on the letterhead somewhere are:

0438 915 267
Max@Tarnbyelectrical.example.au
PO Box 817 Marrowvale NSW 2190
ABN: 57 318 962 407

Thanks!

```html
<!DOCTYPE html>
<html lang="en">
<head>
<meta charset="utf-8">
<title>Tarnby Group Letterhead</title>
<link rel="stylesheet" href="https://fonts.googleapis.com/css2?family=Lato:wght@400;700;900&family=Arimo:wght@400&display=swap">
<style>
  :root {
    --brand-orange: #f05523;
    --ink-black: #1b1b1b;
    --text-dark: #111111;
    --paper: #ffffff;
  }
  * { margin: 0; padding: 0; box-sizing: border-box; }
  html, body {
    width: 927px;
    height: 1200px;
    overflow: hidden;
    background: var(--paper);
  }
  .letterhead {
    position: relative;
    width: 927px;
    height: 1200px;
    background: var(--paper);
  }
  .frame-art {
    position: absolute;
    inset: 0;
    width: 927px;
    height: 1200px;
  }
  .frame-line {
    fill: none;
    stroke: var(--brand-orange);
    stroke-width: 4.5;
  }
  .block-black { fill: var(--ink-black); }
  .block-orange { fill: var(--brand-orange); }
  .brand-mark {
    fill: none;
    stroke: var(--ink-black);
    stroke-width: 4.5;
  }
  .brand-name {
    position: absolute;
    left: 56px;
    top: 152px;
    width: 210px;
    text-align: center;
    font-family: "Lato", sans-serif;
    font-weight: 900;
    font-size: 22px;
    letter-spacing: 0.5px;
    color: var(--ink-black);
    text-transform: uppercase;
  }
  .letter-body {
    position: absolute;
    left: 144px;
    top: 404px;
    font-family: "Lato", sans-serif;
    font-size: 16.4px;
    line-height: 21.8px;
    color: var(--text-dark);
  }
  .contact-block {
    position: absolute;
    right: 56px;
    top: 1021px;
    text-align: right;
    font-family: "Arimo", sans-serif;
    font-size: 13.4px;
    line-height: 18.2px;
    color: var(--text-dark);
  }
</style>
</head>
<body>
<main class="letterhead">
  <svg class="frame-art" viewBox="0 0 927 1200" aria-hidden="true">
    <polyline class="frame-line" points="927,57.5 280,57.5 280,216.6 56,216.6 56,1200"/>
    <polyline class="frame-line" points="868,0 868,980 642,980 642,1139 0,1139"/>
    <rect class="block-black" x="295" y="70" width="54.5" height="54.5"/>
    <rect class="block-orange" x="353" y="127" width="33" height="33"/>
    <rect class="block-orange" x="542" y="1039" width="33" height="33"/>
    <rect class="block-black" x="579" y="1074" width="54.5" height="54.5"/>
    <circle class="brand-mark" cx="161" cy="106" r="31"/>
  </svg>

  <div class="brand-name">Tarnby Group</div>

  <section class="letter-body">
    <p>Lorem ipsum dolor sit amet, consectetur adipiscing elit.</p>
    <p>Pellentesque id libero bibendum, ultrices neque placerat, condimentum metus.</p>
    <p>Nunc rhoncus est aliquam urna finibus, eget imperdiet velit varius.</p>
    <p>Etiam ornare ligula at viverra mollis.</p>
    <p>Maecenas scelerisque massa ac tortor bibendum, eget luctus nunc aliquam.</p>
    <p>Maecenas auctor lacus eget ornare elementum.</p>
    <p>Suspendisse sed augue quis urna malesuada ultricies ac ut nunc.</p>
    <p>Morbi suscipit justo a viverra pretium.</p>
    <p>Praesent a leo non orci tempus imperdiet.</p>
    <p>Proin sit amet mi nec ante laoreet sollicitudin eget in lacus.</p>
    <p>Cras malesuada eros vitae luctus pellentesque.</p>
    <p>Maecenas a nunc sagittis eros dapibus condimentum.</p>
    <p>In volutpat sapien vel lorem pharetra, vitae luctus dolor feugiat.</p>
    <p>Sed sollicitudin metus sit amet risus tristique pretium.</p>
    <p>Integer id nunc et eros mattis varius.</p>
    <p>Praesent mollis erat id orci dictum feugiat.</p>
  </section>

  <address class="contact-block" style="font-style: normal;">
    <p>0438 915 267</p>
    <p>Max@Tarnbyelectrical.example.au</p>
    <p>PO Box 817 Marrowvale NSW 2190</p>
    <p>ABN: 57 318 962 407</p>
  </address>
</main>
</body>
</html>
```